New website for our Escape Room

We are wanting to create a new website for our website. We have 2 different locations that guests will choose their location on the home page. Then we have 5 different escape room experiences. We like clean and fresh but fun. Our logo is black white and red. We like a modern feel that is simple to navigate. I love movement on the page. You can see our current site at lockwickpuzzlehall.example
We like fresh and modern. It needs to include much of the same information as out current site but we won't like the look of our site.

Target Market(s)

amusement, escape rooms.

Industry/Entity Type

escape room

Number of Pages Required

4 page

Requirements
Must have
• info on all 4 escape rooms, option to choose between Pigeon Forge and Nashville locations.

```html
<!DOCTYPE html>
<html lang="en">
<head>
<meta charset="utf-8">
<title>Lockwick – Escape Rooms for Every Party</title>
<link rel="stylesheet" href="https://fonts.googleapis.com/css2?family=Bebas+Neue&family=Barlow+Condensed:wght@500;600&family=Barlow:wght@400;500;600&display=swap">
<style>
:root{
  --red:#e0131c;
  --red-deep:#8a0006;
  --black:#000;
  --ink:#111;
  --panel:#1c1c1c;
  --grey:#2a2a2a;
  --grey-light:#8d8d8d;
  --white:#fff;
  --muted:#bdbdbd;
  --display:"Bebas Neue",sans-serif;
  --cond:"Barlow Condensed",sans-serif;
  --body:"Barlow",sans-serif;
}
*{margin:0;padding:0;box-sizing:border-box}
html,body{width:1200px;height:3781px;overflow:hidden;background:var(--black);color:var(--white);font-family:var(--body)}
.page{position:relative;width:1200px;height:3781px;overflow:hidden}
.abs{position:absolute}
.center{text-align:center}

/* header */
.site-header{position:absolute;left:0;top:0;width:1200px;height:86px;background:var(--black);border-bottom:1px solid #333;z-index:5}
.brand{position:absolute;display:flex;align-items:center;gap:8px;font-family:var(--display);letter-spacing:1px;color:var(--white)}
.brand-mark{width:10px;height:10px;background:var(--red)}
.site-header .brand{left:117px;top:14px;font-size:54px}
.nav{position:absolute;top:33px;left:384px;display:flex;gap:0;font-family:var(--cond);font-weight:600;font-size:17px}
.nav a{color:var(--white);text-decoration:none;position:absolute;white-space:nowrap}
.nav .active::after{content:"";position:absolute;left:-4px;right:-4px;top:34px;height:3px;background:var(--red)}
.btn-contact{position:absolute;left:948px;top:23px;width:142px;height:43px;border:3px solid var(--red);font-family:var(--cond);font-weight:600;font-size:17px;display:flex;align-items:center;justify-content:center}

/* hero */
.hero-visual{left:0;top:86px;width:1200px;height:680px;background:radial-gradient(ellipse 190px 420px at 612px 260px,#b3121b 0%,#6e0a10 45%,rgba(0,0,0,0) 100%),linear-gradient(180deg,#000 0%,#230607 40%,#4a0a0d 80%,#2a0709 100%)}
.hero-title{left:0;width:1200px;top:250px;font-family:var(--display);font-size:128px;line-height:1;letter-spacing:8px}
.hero-sub{left:0;width:1200px;top:372px;font-family:var(--display);font-size:52px;letter-spacing:4px}
.btn-pill{left:490px;top:445px;width:236px;height:61px;border:2px solid var(--white);border-radius:31px;font-family:var(--cond);font-weight:500;font-size:19px;letter-spacing:2px;display:flex;align-items:center;justify-content:center}

/* locations */
.loc-left{left:0;top:700px;width:612px;height:620px;background:radial-gradient(ellipse 260px 260px at 170px 330px,#e3141e 0%,#8d0308 55%,#3a0003 100%)}
.loc-right{left:612px;top:700px;width:588px;height:620px;background:radial-gradient(ellipse 320px 300px at 300px 320px,#4a4a4a 0%,#252525 60%,#141414 100%)}
.loc-name{font-family:var(--display);font-size:56px;letter-spacing:4px;width:500px}
.loc-text{font-size:19px;line-height:23px;width:500px}
.btn-box{border:2px solid var(--white);font-family:var(--cond);font-weight:600;font-size:16px;display:flex;align-items:center;justify-content:center;letter-spacing:.5px}

/* rooms */
.rooms-bg{left:0;top:1320px;width:1200px;height:800px;background:linear-gradient(180deg,#000 0%,#000 40%,#2f2f2f 75%,#1a1a1a 100%)}
.eyebrow{font-family:var(--display);color:var(--red);font-size:29px;letter-spacing:2px;left:0;width:1200px}
.section-title{font-family:var(--display);font-size:44px;letter-spacing:3px;left:0;width:1200px}
.rule{height:3px;background:#9a9a9a;width:62px}
.diamond{width:240px;height:240px;transform:rotate(45deg);background:linear-gradient(135deg,#3a3a3a,#151515);border:2px solid #6d6d6d;outline:7px solid rgba(60,60,60,.8)}
.diamond.featured{background:linear-gradient(135deg,#c2111a,#5b0004);border-color:#f0505a;outline-color:rgba(224,19,28,.6)}
.diamond.small{width:226px;height:226px}
.room-label{font-family:var(--display);font-size:31px;letter-spacing:1.5px;width:260px;text-align:center}

/* benefits */
.band-red{left:0;top:2060px}
.benefits{left:0;top:2185px;width:1200px;height:620px;background:var(--grey)}
.ghost{font-family:var(--display);color:rgba(255,255,255,.06);left:0;width:1200px;text-align:center;letter-spacing:6px}
.benefit-num{font-family:var(--cond);color:var(--red);font-size:21px;font-weight:500}
.benefit-text{font-family:var(--cond);font-weight:600;font-size:17px;line-height:22px;letter-spacing:.2px}
.core-visual{left:410px;top:2510px;width:380px;height:380px;border-radius:50%;background:radial-gradient(circle at 50% 55%,#d1121c 0%,#7a0006 60%,#3a0003 100%);border:10px solid #3d3d3d}

/* who */
.who{left:0;top:2805px;width:1200px;height:530px;background:linear-gradient(180deg,#2a2a2a 0%,#141414 100%)}
.card{width:246px;height:252px;border:1.5px solid #555;background:rgba(30,30,30,.6);clip-path:polygon(28px 0,100% 0,100% calc(100% - 28px),calc(100% - 28px) 100%,0 100%,0 28px)}
.card-title{font-family:var(--display);font-size:26px;letter-spacing:1px;text-align:center;width:100%;position:absolute;top:98px}
.card-text{font-size:12px;line-height:15px;color:#ddd;text-align:center;width:180px;left:33px;position:absolute;top:128px}
.card .btn-box{position:absolute;left:68px;top:188px;width:112px;height:32px;font-size:13px;border-width:1.5px}

/* footer */
.footer{left:0;top:3465px;width:1200px;height:316px;background:var(--ink)}
.footer-col-title{font-family:var(--cond);font-weight:600;font-size:23px}
.footer-link{font-size:13px;color:#ddd;line-height:23px}
.footer-small{font-size:12px;color:#aaa;line-height:19px}
.footer-contact{font-size:12.5px;color:#ddd;line-height:23px}
.footer-contact strong{color:var(--white);font-weight:600;font-size:14px}
.social{width:34px;height:34px;border-radius:50%;background:var(--white)}
.social.red{background:var(--red)}
</style>
</head>
<body>
<div class="page">

  <header class="site-header">
    <div class="brand"><span class="brand-mark"></span>LOCKWICK</div>
    <nav class="nav">
      <a class="active" style="left:0">ABOUT US</a>
      <a style="left:100px">ESCAPE ROOMS</a>
      <a style="left:250px">FAQ</a>
      <a style="left:329px">GALLERY</a>
      <a style="left:441px">GIFT CARDS</a>
    </nav>
    <div class="btn-contact">CONTACT US</div>
  </header>

  <!-- hero -->
  <div class="abs hero-visual" role="img" aria-label="Dark red keyhole scene with a lone figure standing at the mouth of a stone maze"></div>
  <div class="abs hero-title center">LOCKWICK</div>
  <div class="abs hero-sub center">ESCAPE ROOMS FOR EVERY PARTY</div>
  <div class="abs btn-pill">FIND YOUR LOCATION</div>

  <!-- locations -->
  <div class="abs loc-left" role="img" aria-label="Red-lit vintage asylum chair in a dark room" style="clip-path:polygon(0 0,100% 60px,100% 555px,0 100%)"></div>
  <div class="abs loc-right" role="img" aria-label="Black and white image of hands reaching toward a ruined city" style="clip-path:polygon(0 60px,100% 0,100% 100%,0 555px)"></div>
  <svg class="abs" style="left:0;top:690px" width="1200" height="90" viewBox="0 0 1200 90">
    <polyline points="0,10 612,70 1200,10" fill="none" stroke="#fff" stroke-width="4"/>
  </svg>
  <svg class="abs" style="left:570px;top:638px" width="62" height="62" viewBox="0 0 62 62">
    <circle cx="31" cy="31" r="29" fill="#fff"/>
    <path d="M31 18v24M22 34l9 9 9-9" fill="none" stroke="#e0131c" stroke-width="2.5" stroke-linecap="round"/>
  </svg>

  <div class="abs loc-name center" style="left:85px;top:932px">NASHVILLE</div>
  <div class="abs loc-text center" style="left:82px;top:1000px">Wheelchair Accessible Rooms at<br>Nashville: Asylum</div>
  <div class="abs btn-box" style="left:272px;top:1070px;width:138px;height:45px">BOOK NOW</div>

  <div class="abs loc-name center" style="left:638px;top:932px">PIGEON FORGE</div>
  <div class="abs loc-text center" style="left:643px;top:1000px">Wheelchair Accessible Rooms at Pigeon<br>Forge: Mobster, Haunted Cabin, Asylum</div>
  <div class="abs btn-box" style="left:827px;top:1070px;width:138px;height:45px">BOOK NOW</div>

  <!-- rooms -->
  <div class="abs rooms-bg" role="img" aria-label="Grey stone maze seen from above fading into darkness" style="clip-path:polygon(0 0,612px 0,100% 0,100% 100%,0 100%)"></div>
  <div class="abs eyebrow center" style="top:1343px">SELECT YOUR ROOM</div>
  <div class="abs section-title center" style="top:1380px">FIND THE RIGHT ROOM FOR YOU</div>
  <div class="abs rule" style="left:586px;top:1440px"></div>

  <div class="abs diamond" style="left:140px;top:1545px"></div>
  <div class="abs diamond featured" style="left:500px;top:1525px"></div>
  <div class="abs diamond" style="left:855px;top:1545px"></div>
  <div class="abs diamond small" style="left:327px;top:1747px"></div>
  <div class="abs diamond small" style="left:689px;top:1747px"></div>

  <div class="abs room-label" style="left:130px;top:1676px">APOCALYPSE</div>
  <div class="abs room-label" style="left:493px;top:1676px">IRON ISLAND</div>
  <div class="abs room-label" style="left:845px;top:1676px">CAPTURED</div>
  <div class="abs room-label" style="left:310px;top:1870px">HAUNTED CABIN</div>
  <div class="abs room-label" style="left:672px;top:1870px">ASYLUM</div>
  <svg class="abs" style="left:607px;top:1728px" width="32" height="20" viewBox="0 0 32 20">
    <path d="M2 10h26M20 3l8 7-8 7" fill="none" stroke="#fff" stroke-width="2"/>
  </svg>

  <!-- band -->
  <svg class="abs band-red" width="1200" height="130" viewBox="0 0 1200 130">
    <rect width="1200" height="130" fill="#2a2a2a"/>
    <polygon points="0,0 612,90 1200,0 1200,130 0,130" fill="#2a2a2a"/>
    <polygon points="0,0 612,90 0,130" fill="#d40f18"/>
    <polygon points="1200,10 612,90 1200,120" fill="#9a9a9a"/>
  </svg>

  <!-- benefits -->
  <div class="abs benefits"></div>
  <div class="abs ghost" style="top:2200px;font-size:88px">DISCOVER</div>
  <div class="abs section-title center" style="top:2256px">THE BENEFITS OF ESCAPE ROOMS</div>

  <div class="abs core-visual" role="img" aria-label="Red-toned photo of many hands reaching for a locked door"></div>
  <div class="abs brand" style="left:478px;top:2650px;font-size:76px"><span class="brand-mark" style="width:14px;height:14px"></span>LOCKWICK</div>
  <div class="abs" style="left:0;top:2805px;width:1200px;height:100px;background:#1e1e1e"></div>

  <svg class="abs" style="left:290px;top:2430px" width="620" height="380" viewBox="0 0 620 380">
    <path d="M20 375 A292 292 0 0 1 600 375" fill="none" stroke="#e0131c" stroke-width="6"/>
    <g fill="#2a2a2a" stroke="#e0131c" stroke-width="3">
      <circle cx="53" cy="207" r="38"/>
      <circle cx="158" cy="72" r="38"/>
      <circle cx="310" cy="20" r="38"/>
      <circle cx="466" cy="72" r="38"/>
      <circle cx="576" cy="207" r="38"/>
    </g>
    <g fill="none" stroke="#fff" stroke-width="2">
      <circle cx="53" cy="207" r="6"/><circle cx="53" cy="207" r="16"/>
      <circle cx="158" cy="72" r="14"/><path d="M150 72h16M158 64v16"/>
      <circle cx="310" cy="18" r="14"/><path d="M302 38h16"/>
      <circle cx="458" cy="72" r="11"/><circle cx="474" cy="72" r="11"/>
      <ellipse cx="576" cy="207" rx="16" ry="9"/><circle cx="576" cy="207" r="4"/>
      <path d="M558 190v-6h6M594 190v-6h-6M558 224v6h6M594 224v6h-6"/>
    </g>
  </svg>

  <div class="abs benefit-num center" style="left:0;width:1200px;top:2338px">03</div>
  <div class="abs benefit-text center" style="left:0;width:1200px;top:2358px">CHALLENGE YOUR CREATIVE THINKING<br>AND PROBLEM SOLVING SKILLS</div>
  <div class="abs benefit-num" style="left:370px;top:2455px">02</div>
  <div class="abs benefit-text" style="left:200px;width:193px;text-align:right;top:2477px">ENHANCE AND BUILD<br>YOUR MEMORY</div>
  <div class="abs benefit-num" style="left:802px;top:2448px">04</div>
  <div class="abs benefit-text" style="left:804px;top:2474px">IMPROVE YOUR MOOD</div>
  <div class="abs benefit-num" style="left:272px;top:2588px">01</div>
  <div class="abs benefit-text" style="left:60px;width:233px;text-align:right;top:2611px">IMPROVE COMMUNICATION<br>AND SOCIAL SKILLS</div>
  <div class="abs benefit-num" style="left:915px;top:2578px">05</div>
  <div class="abs benefit-text" style="left:916px;top:2600px">INCREASE YOUR<br>ATTENTION TO DETAIL</div>

  <!-- who -->
  <div class="abs who"></div>
  <div class="abs ghost" style="top:2855px;font-size:88px">WHO COME</div>
  <div class="abs section-title center" style="top:2892px">LOCKWICK WHO</div>
  <svg class="abs" style="left:200px;top:2975px" width="800" height="25" viewBox="0 0 800 25">
    <path d="M5 22V3H793V22M262 3V22M527 3V22" fill="none" stroke="#bbb" stroke-width="2"/>
  </svg>

  <div class="abs card" style="left:72px;top:3010px">
    <div class="card-title">TEAM BUILDING</div>
    <div class="card-text">What better way to foster synergy and teamwork than to be locked in a room together?</div>
    <div class="btn-box">LEARN MORE</div>
  </div>
  <div class="abs card" style="left:336px;top:3010px">
    <div class="card-title">GAMERS</div>
    <div class="card-text">What better way to foster synergy and teamwork than to be locked in a room together?</div>
    <div class="btn-box">LEARN MORE</div>
  </div>
  <div class="abs card" style="left:606px;top:3010px">
    <div class="card-title">FRIENDS AND FAMILY</div>
    <div class="card-text">What better way to foster synergy and teamwork than to be locked in a room together?</div>
    <div class="btn-box">LEARN MORE</div>
  </div>
  <div class="abs card" style="left:868px;top:3010px">
    <div class="card-title">TOURISTS AND VISITOR</div>
    <div class="card-text">What better way to foster synergy and teamwork than to be locked in a room together?</div>
    <div class="btn-box">LEARN MORE</div>
  </div>

  <!-- band -->
  <svg class="abs" style="left:0;top:3335px" width="1200" height="130" viewBox="0 0 1200 130">
    <rect width="1200" height="130" fill="#141414"/>
    <polygon points="0,0 600,90 0,130" fill="#d40f18"/>
    <polygon points="1200,10 600,90 1200,120" fill="#555"/>
    <rect y="125" width="1200" height="5" fill="#111"/>
  </svg>
  <svg class="abs" style="left:568px;top:3393px" width="64" height="64" viewBox="0 0 64 64">
    <circle cx="32" cy="32" r="29" fill="#fff" stroke="#111" stroke-width="3"/>
    <path d="M32 44V20M23 28l9-9 9 9" fill="none" stroke="#e0131c" stroke-width="2.5" stroke-linecap="round"/>
  </svg>

  <!-- footer -->
  <footer class="abs footer">
    <div class="abs brand" style="left:128px;top:58px;font-size:56px"><span class="brand-mark"></span>LOCKWICK</div>
    <div class="abs social red" style="left:133px;top:130px" aria-label="Social profile"></div>
    <div class="abs social" style="left:176px;top:130px" aria-label="Social profile"></div>
    <div class="abs social" style="left:219px;top:130px" aria-label="Social profile"></div>
    <div class="abs social" style="left:262px;top:130px" aria-label="Social profile"></div>
    <div class="abs footer-small" style="left:130px;top:188px">© 2022 Lockwick &nbsp;All Rights Reserved<br>Terms &amp; Condition &nbsp;Privacy Policy</div>

    <div class="abs" style="left:420px;top:30px;width:1px;height:286px;background:#2e2e2e"></div>
    <div class="abs" style="left:420px;top:48px;width:3px;height:26px;background:var(--red)"></div>
    <div class="abs footer-col-title" style="left:450px;top:45px">QUICK LINKS</div>
    <div class="abs footer-link" style="left:455px;top:94px">About Us<br>Gallery<br>Escape Rooms<br>FAQ<br>Find your location<br>Contact Us</div>

    <div class="abs" style="left:650px;top:30px;width:1px;height:286px;background:#2e2e2e"></div>
    <div class="abs" style="left:650px;top:48px;width:3px;height:26px;background:var(--red)"></div>
    <div class="abs footer-col-title" style="left:677px;top:45px">CONTACT US</div>
    <div class="abs footer-contact" style="left:677px;top:92px"><strong>Nashville</strong><br>P: 555-014-2200<br>nashville@lockwickpuzzlehall.example<br>118 Harlow Lane, Nashville,<br>TN 37000</div>
    <div class="abs footer-contact" style="left:915px;top:92px"><strong>Pigeon Forge</strong><br>P: 555-018-7300<br>info@lockwickpuzzlehall.example<br>740 Ridgeview Road, Suite 9,<br>Pigeon Forge, TN 37800</div>
  </footer>

</div>
</body>
</html>
```